Dot's Dash: Poster Art Design For A New Musical

We are a non-profit educational theatre company producing a new musical called "Dot's Dash"- a modern retelling of the classic Milo Brandvik poem. This upbeat musical comedy features kids in a little league championship tournament and is about teamwork, personal growth and girl power. We are seeking a designer to design a poster for the upcoming production. This poster should include name/logo artwork as well as a full graphic thought for the full image.
Updates

Went on vacation/holiday

Target Market(s)

Teenagers and their parents interested in musical theatre. Edgy but wholesome

Industry/Entity Type

Musical Theatre- sophisticated, Broadway, texture and layers (not kiddie)

Requirements
Must have
• Name of the Show: Dot's Dash
Nice to have
• Baseball themed, A picture of a young girl up at bat, fun colors but photo based, images inside of images, a clean layout, high school appeal

```html
<!DOCTYPE html>
<html lang="en">
<head>
<meta charset="utf-8">
<title>Dot's Dash – Musical Poster</title>
<link rel="stylesheet" href="https://fonts.googleapis.com/css2?family=Montserrat:wght@300;400;600;700;800&family=Great+Vibes&display=swap">
<style>
  :root {
    --night: #0d1f33;
    --deep-teal: #123a4c;
    --teal: #1c8e9a;
    --aqua: #5fd4dc;
    --mauve: #b14f86;
    --mauve-dark: #8e3a6b;
    --white: #ffffff;
    --soft-white: #e9eef4;
  }
  * { margin: 0; padding: 0; box-sizing: border-box; }
  html, body { width: 900px; height: 1200px; overflow: hidden; background: var(--night); }
  .poster {
    position: relative;
    width: 900px;
    height: 1200px;
    overflow: hidden;
    font-family: "Montserrat", Arial, sans-serif;
    color: var(--white);
    background:
      radial-gradient(circle at 30% 85%, rgba(95,212,220,0.35) 0, rgba(95,212,220,0) 40%),
      radial-gradient(circle at 85% 15%, rgba(95,212,220,0.3) 0, rgba(95,212,220,0) 35%),
      radial-gradient(circle at 70% 95%, rgba(177,79,134,0.25) 0, rgba(177,79,134,0) 40%),
      linear-gradient(160deg, var(--deep-teal) 0%, var(--night) 55%, #0a1626 100%);
  }
  .shapes { position: absolute; inset: 0; }
  .title-block {
    position: absolute;
    right: 50px;
    top: 555px;
    text-align: right;
  }
  .title-kicker {
    font-family: "Great Vibes", cursive;
    color: var(--aqua);
    font-size: 118px;
    line-height: 1;
    margin-right: 20px;
  }
  .show-name {
    font-weight: 700;
    font-size: 80px;
    line-height: 1;
    letter-spacing: 1px;
    margin-top: -14px;
  }
  .author {
    font-weight: 300;
    font-size: 27px;
    letter-spacing: 1px;
    margin-top: 26px;
    color: var(--soft-white);
  }
  .info {
    position: absolute;
    left: 66px;
    top: 868px;
    width: 470px;
  }
  .info-heading { font-weight: 700; font-size: 44px; letter-spacing: 1px; line-height: 1; }
  .info-invite { font-weight: 400; font-size: 36px; margin-top: 28px; line-height: 1; }
  .info-body {
    font-weight: 400;
    font-size: 20px;
    line-height: 1.4;
    margin-top: 22px;
    text-transform: uppercase;
  }
  .dates {
    position: absolute;
    right: 36px;
    top: 972px;
    text-align: right;
    font-weight: 700;
    font-size: 50px;
    line-height: 1.2;
  }
</style>
</head>
<body>
<main class="poster">
  <svg class="shapes" width="900" height="1200" viewBox="0 0 900 1200">
    <defs>
      <linearGradient id="batterPhoto" x1="0" y1="0" x2="0.6" y2="1">
        <stop offset="0" stop-color="#8fb6a0"/>
        <stop offset="0.45" stop-color="#6f8f6a"/>
        <stop offset="0.75" stop-color="#8a5fb0"/>
        <stop offset="1" stop-color="#c2a78a"/>
      </linearGradient>
      <radialGradient id="micPhoto" cx="0.5" cy="0.45" r="0.6">
        <stop offset="0" stop-color="#c9c2b8"/>
        <stop offset="0.5" stop-color="#a0622e"/>
        <stop offset="1" stop-color="#4a2412"/>
      </radialGradient>
      <clipPath id="posterClip"><rect width="900" height="1200"/></clipPath>
    </defs>
    <g clip-path="url(#posterClip)">
      <!-- mauve feature disc -->
      <circle class="feature-disc" cx="800" cy="520" r="430" fill="var(--mauve)"/>
      <circle class="feature-ring" cx="800" cy="520" r="450" fill="none" stroke="var(--night)" stroke-width="4" opacity="0.6"/>
      <!-- batter photo frame -->
      <circle class="batter-ring" cx="220" cy="280" r="330" fill="var(--teal)"/>
      <circle class="batter-photo" cx="220" cy="280" r="312" fill="url(#batterPhoto)" role="img" aria-label="Photo of a young girl in a purple tutu at bat on a baseball field"/>
      <!-- microphone photo frame -->
      <circle class="mic-ring" cx="560" cy="222" r="134" fill="var(--teal)"/>
      <circle class="mic-photo" cx="560" cy="222" r="120" fill="url(#micPhoto)" role="img" aria-label="Close-up photo of a vintage stage microphone"/>
    </g>
  </svg>

  <section class="title-block">
    <div class="title-kicker">Musical</div>
    <h1 class="show-name">DOT'S DASH</h1>
    <p class="author">MILO BRANDVIK</p>
  </section>

  <section class="info">
    <h2 class="info-heading">LOREM IPSUM</h2>
    <p class="info-invite">JOIN US</p>
    <p class="info-body">Lorem ipsum dolor sit amet, consectetur adipiscing elit, sed do eiusmod tempor incididunt ut labore et</p>
  </section>

  <section class="dates">
    <p>NOV 2023</p>
    <p>DEC 2023</p>
  </section>
</main>
</body>
</html>
```